Small soho-London based IT Support company website

We've had our logo and stationary redesigned on Sketch Harbor and now we'd like our website done.
We're a small IT support company. Our client base is mainly design studios and advertising agencies working mainly on Macs.
As such our website needs to be young clean and professional looking.
Our current site can be viewed at http://brisk-node.example
We currently use Joomla but we're happy to move to Wordpress if that's the only option.
Industry/Entity Type
Advertising
Look and feel
Each slider illustrates characteristics of the customer's brand and the style your logo design should communicate.

```html
<!DOCTYPE html>
<html lang="en">
<head>
<meta charset="utf-8">
<title>Brisk Node – IT Support</title>
<link href="https://fonts.googleapis.com/css2?family=Didact+Gothic&family=Open+Sans:wght@400;600;700&family=Ubuntu:wght@400;500;700&display=swap" rel="stylesheet">
<style>
:root{
  --dark:#2b2b2b;
  --dark-2:#4a4a4a;
  --lime:#b3d41a;
  --lime-light:#c9e326;
  --lime-deep:#8fae0c;
  --text:#555;
  --panel:#f6f5f1;
  --line:#d8d8d2;
  --white:#fff;
}
*{margin:0;padding:0;box-sizing:border-box}
html,body{width:1100px;height:1200px;overflow:hidden;background:var(--white)}
body{position:relative;font-family:"Didact Gothic",sans-serif;color:var(--text)}
.abs{position:absolute}

.site-header{left:0;top:0;width:1100px;height:114px;background:linear-gradient(#444,#262626)}
.brand{left:72px;top:24px;font:700 58px/1 "Ubuntu",sans-serif;color:var(--lime);letter-spacing:-1px}
.brand-dot{display:inline-block;width:14px;height:14px;background:var(--lime);border-radius:50%;margin-left:8px;vertical-align:top;margin-top:8px}
.call{left:905px;top:6px;color:#ddd;font-size:23px}
.call-icon{left:864px;top:1px}
.phone{left:868px;top:31px;color:#ddd;font-size:24px;letter-spacing:1px}
.main-nav{left:566px;top:82px;display:flex;font:700 11.5px/32px "Open Sans",sans-serif}
.main-nav a{color:var(--white);text-decoration:none;display:block;height:32px;text-transform:uppercase}
.main-nav .active{background:var(--lime);padding:0 13px;width:60px}

.hero{left:0;top:114px;width:1100px;height:307px;background:linear-gradient(135deg,var(--lime-light),var(--lime-deep))}
.hero-photo{left:57px;top:125px;width:646px;height:280px;border:5px solid var(--white);box-shadow:0 1px 4px rgba(0,0,0,.3);background:linear-gradient(90deg,#4b6f8f 0%,#c9c2b0 35%,#f2f2f2 60%,#d9d9d9 100%)}
.hero-title{left:718px;top:142px;font:700 44px/1 "Ubuntu",sans-serif;color:#111;-webkit-text-stroke:1px #fff}
.hero-text{left:717px;top:214px;width:314px;color:var(--white);font:12px/20px "Open Sans",sans-serif;letter-spacing:-.25px;text-align:justify}
.btn-more{left:721px;top:373px;width:105px;height:31px;border-radius:16px;background:linear-gradient(#fff,#cfcfcf);color:#333;font:600 14px/31px "Open Sans",sans-serif;text-align:center}

.col-head{height:31px;width:295px;border-radius:16px;background:linear-gradient(#6a6a6a,#1f1f1f);color:var(--white);font:400 21px/31px "Ubuntu",sans-serif;padding-left:50px}
.col-icon{width:44px;height:44px;border-radius:50%;background:radial-gradient(circle at 35% 30%,#9fd0ff,#1a5fae)}
.col-photo{width:288px;height:115px;border:1px solid #ccc;padding:3px}
.col-photo div{width:100%;height:100%}
.col-text{width:290px;font-size:11.5px;line-height:18px;text-align:justify;letter-spacing:.3px}
.col-text .gap{margin-top:18px}
.services{list-style:none;margin-top:9px}
.services li{position:relative;padding-left:10px}
.services li::before{content:"";position:absolute;left:-3px;top:6px;border-left:4px solid #333;border-top:3px solid transparent;border-bottom:3px solid transparent}

.location{left:57px;top:834px;width:650px;height:303px;background:var(--panel);border:1px solid var(--line);border-radius:12px}
.map{left:72px;top:849px;width:361px;height:278px;border:5px solid var(--white);box-shadow:0 0 2px rgba(0,0,0,.3);background:linear-gradient(135deg,#e8e4d8,#f3d69a 50%,#e2dfd4)}
.loc-title{left:450px;top:862px;color:var(--lime-deep);font:400 22px/1 "Ubuntu",sans-serif;letter-spacing:1px}
.loc-text{left:446px;top:896px;width:241px;font:11.5px/20px "Open Sans",sans-serif;letter-spacing:-.15px;text-align:justify}
.postcode-label{left:446px;top:1064px;font:12.5px/1 "Open Sans",sans-serif;color:#333}
.field{height:23px;background:var(--white);border:1px solid #bbb}
.search{left:661px;top:1087px}

.quote{left:728px;top:832px;width:303px;height:300px;border-radius:20px;background:linear-gradient(#8fae0c,var(--lime-light))}
.quote-title{left:751px;top:838px;color:var(--white);font:500 19px/1 "Ubuntu",sans-serif}
.q-label{color:var(--white);font:12.5px/1 "Open Sans",sans-serif;text-align:right;width:70px}
.q-field{width:146px;height:19px;background:var(--white);border:1px solid #999}
.spin{position:absolute;right:0;top:0;width:12px;height:17px;border-left:1px solid #ccc}
.spin::before,.spin::after{content:"";position:absolute;left:3px;border-left:3px solid transparent;border-right:3px solid transparent}
.spin::before{top:3px;border-bottom:3px solid #444}
.spin::after{bottom:3px;border-top:3px solid #444}
.check{width:22px;height:18px;background:linear-gradient(#fff,#ddd);border:1px solid #999}
.check-label{color:var(--white);font:12.5px/1 "Open Sans",sans-serif;letter-spacing:.3px}
.btn-learn{left:916px;top:1097px;width:88px;height:22px;border-radius:11px;background:linear-gradient(#555,#222);color:var(--white);font:12.5px/22px "Open Sans",sans-serif;text-align:center}

.site-footer{left:0;top:1149px;width:1100px;height:51px;background:linear-gradient(#444,#2a2a2a);color:var(--white);text-align:center;font-size:12.5px;letter-spacing:.6px}
.foot-nav{margin-top:6px}
.foot-nav span{margin:0 9px}
.copy{margin-top:6px}
</style>
</head>
<body>

<header class="abs site-header"></header>
<div class="abs brand">BriskNode<span class="brand-dot"></span></div>
<svg class="abs call-icon" width="34" height="34" viewBox="0 0 34 34"><circle cx="17" cy="17" r="16" fill="#a9cc12"/><rect x="9" y="11" width="16" height="12" fill="none" stroke="#fff" stroke-width="1.5"/><path d="M9 11l8 7 8-7" fill="none" stroke="#fff" stroke-width="1.5"/></svg>
<div class="abs call">Call us Today</div>
<div class="abs phone">555-0142-7788</div>
<nav class="abs main-nav">
  <a class="active" href="#">Home</a>
  <a href="#" style="margin-left:35px">About Us</a>
  <a href="#" style="margin-left:58px">Services</a>
  <a href="#" style="margin-left:51px">Why Us</a>
  <a href="#" style="margin-left:53px">Contact</a>
</nav>

<section class="abs hero"></section>
<div class="abs hero-photo" role="img" aria-label="Photo of a globe connected by cable to a computer mouse under a hand"></div>
<h1 class="abs hero-title">Hello!</h1>
<p class="abs hero-text">Lorem ipsum dolor sit consectetuer adipiscing Praesent vestibulum aenean nonummyhendrerit mauris. Hasellus porta aenean nonummyhendrerit mauris aenean nonummyhendrerit mauris. Hasellus porta. Fusce suscipit varius mi. Cum sociis natoque penatibus et magnis dis parturient.</p>
<div class="abs btn-more">MORE INFO</div>

<div class="abs col-head" style="left:62px;top:440px">ORION</div>
<div class="abs col-icon" style="left:62px;top:433px"></div>
<div class="abs col-photo" style="left:67px;top:485px"><div role="img" aria-label="Three smartphones showing app screens" style="background:linear-gradient(90deg,#fff,#444 20%,#fff 40%,#555 60%,#fff 80%,#333)"></div></div>
<div class="abs col-text" style="left:76px;top:610px">
  <p>We have over 50 combined years in supporting Orion systems.</p>
  <p>Our Orion specialists speak plain English so you're not left baffled by computer jargon.</p>
  <ul class="services"><li>SME &amp; Corporate Networks</li><li>Kestrel Email Server</li><li>Bespoke Applications</li><li>Web Services</li><li>Connectivity</li><li>Security</li></ul>
</div>

<div class="abs col-head" style="left:393px;top:440px;padding-left:77px">PC</div>
<div class="abs col-icon" style="left:395px;top:434px;border-radius:4px;width:58px;height:40px;background:linear-gradient(#9cc6ee,#2c5c8c)"></div>
<div class="abs col-photo" style="left:398px;top:485px"><div role="img" aria-label="Banner for a bespoke IT solutions partner with a person using a laptop" style="background:linear-gradient(90deg,#9ecde6,#f4f4f4 35%,#fff)"></div></div>
<div class="abs col-text" style="left:405px;top:607px">
  <p>Friendly Desktop techs with years of industry experience.</p>
  <p>Friendly Desktop techs with years of industry experience.</p>
  <ul class="services"><li>SME &amp; Corporate Networks</li><li>Kestrel Email Server</li><li>Bespoke Applications</li><li>Web Services</li><li>Connectivity</li><li>Security</li></ul>
</div>

<div class="abs col-head" style="left:716px;top:440px;padding-left:71px;width:303px">Combined</div>
<div class="abs col-icon" style="left:718px;top:432px;border-radius:4px;width:48px;height:46px;background:linear-gradient(#7db8ea,#1e4f8a)"></div>
<div class="abs col-photo" style="left:730px;top:485px"><div role="img" aria-label="Collage of IT hardware and device icons" style="background:linear-gradient(90deg,#555,#9ab 30%,#2c7fc7 55%,#4bb 80%,#384)"></div></div>
<div class="abs col-text" style="left:730px;top:611px;width:286px">
  <p>Using both Orions &amp; PC's can be tricky but not with us.</p>
  <p class="gap">Brisk is a joint venture between two IT directors, one Orion focused and one PC focused but both with proven track records in running successful IT supports firms.</p>
  <p class="gap">Our engineers are specialists not all rounders. This means you get the correct fix not a hack.</p>
</div>

<section class="abs location"></section>
<div class="abs map" role="img" aria-label="Street map of Soho and Covent Garden showing the office location"></div>
<h2 class="abs loc-title">Location</h2>
<p class="abs loc-text">This map shows where we are, smack bang in the middle of Soho and Covent Garden. Type your postcode in to see how close we are to your offices. map shows where we are, smack bang in the middle of Soho and Covent Garden. Type your postcode in to see how close we are to your offices.</p>
<div class="abs postcode-label">Enter your post code :</div>
<div class="abs field" style="left:587px;top:1059px;width:102px"></div>
<svg class="abs search" width="30" height="30" viewBox="0 0 30 30"><circle cx="15" cy="15" r="14" fill="#8fbf1a"/><circle cx="13" cy="13" r="5.5" fill="none" stroke="#fff" stroke-width="2"/><path d="M17 17l5 5" stroke="#fff" stroke-width="3" stroke-linecap="round"/></svg>

<section class="abs quote"></section>
<h2 class="abs quote-title">Insti-Quote</h2>
<div class="abs q-label" style="left:738px;top:880px">Laptops :</div>
<div class="abs q-field" style="left:814px;top:876px"><span class="spin"></span></div>
<div class="abs q-label" style="left:738px;top:906px">Desktops :</div>
<div class="abs q-field" style="left:814px;top:902px"><span class="spin"></span></div>
<div class="abs q-label" style="left:738px;top:932px">Servers :</div>
<div class="abs q-field" style="left:814px;top:928px"><span class="spin"></span></div>
<div class="abs check" style="left:785px;top:970px"></div>
<div class="abs check-label" style="left:817px;top:972px">Remote support</div>
<div class="abs check" style="left:785px;top:996px"></div>
<div class="abs check-label" style="left:817px;top:999px">Server Monitoring</div>
<div class="abs check-label" style="left:745px;top:1033px">Monthly Estimate :</div>
<div class="abs field" style="left:746px;top:1058px;width:243px"></div>
<div class="abs btn-learn">Learn More</div>

<footer class="abs site-footer">
  <div class="foot-nav">Home <span>|</span> About Us <span>|</span> Services <span>|</span> Why Us <span>|</span> Contact</div>
  <div class="copy">© Brisk Node Ltd 2011</div>
</footer>

</body>
</html>
```